Security business needs NDA formatted.

We need our NDA formatted properly and to look modern with our logo. Anybody can paste words into a document, but we need something clean, modern, DocuSign-friendly, and stylish.

```html
<!DOCTYPE html>
<html lang="en">
<head>
<meta charset="utf-8">
<title>Meridane – Non-Disclosure Agreement Layout</title>
<link href="https://fonts.googleapis.com/css2?family=Montserrat:wght@300;400;600;700&display=swap" rel="stylesheet">
<style>
:root{
  --backdrop:#c8c9c8;
  --paper:#ffffff;
  --ink:#333333;
  --ink-soft:#555555;
  --cover-bg:#3a3a3a;
  --cover-disc:#0d0d0d;
  --muted:#9a9a9a;
  --edge:#a9a9a9;
}
*{margin:0;padding:0;box-sizing:border-box}
html,body{width:678px;height:1200px;overflow:hidden;background:var(--backdrop)}
body{font-family:"Montserrat",sans-serif;color:var(--ink);font-weight:300}
.sheet{position:absolute;left:0;top:0;width:1456px;height:2576px;transform:scale(.465659);transform-origin:0 0;background:var(--backdrop)}
.page{position:absolute;width:398px;height:562px;background:var(--paper);border:1px solid var(--edge)}
.frame{position:absolute;left:30px;top:32px;width:332px;height:496px;border:3px solid var(--ink);overflow:hidden;padding:20px 14px 10px 0}
.page-footer{position:absolute;left:30px;right:30px;bottom:12px;height:12px}
.footer-brand{position:absolute;left:0;top:0;display:flex;align-items:center;gap:3px;font-size:6px;font-weight:600;color:var(--muted)}
.footer-dot{width:11px;height:11px;border-radius:50%;background:#cfcfcf}
.page-number{position:absolute;right:0;top:0;width:11px;height:11px;border-radius:50%;background:#777;color:#fff;font-size:5px;line-height:11px;text-align:center;font-weight:600}

/* cover */
.cover-panel{position:absolute;left:32px;top:32px;width:332px;height:497px;background:var(--cover-bg)}
.cover-brand{position:absolute;left:0;right:0;top:92px;display:flex;justify-content:center;align-items:center;gap:6px;color:#111;font-weight:600;font-size:16px}
.cover-brand .brand-dot{width:26px;height:26px;border-radius:50%;background:#111}
.cover-disc{position:absolute;left:38px;top:179px;width:256px;height:256px;border-radius:50%;background:var(--cover-disc);display:flex;align-items:center;justify-content:center;text-align:center;color:#fff;font-weight:300;font-size:22px;line-height:27px;letter-spacing:.3px}

/* agreement title page */
.title-block{position:absolute;left:0;right:0;text-align:center}
.doc-title{top:146px;font-size:8.5px;font-weight:400}
.doc-sub{font-size:6px}
.dated-line{position:absolute;left:22px;top:184px;font-size:6.5px}
.band{position:absolute;height:11px;background:var(--ink);color:#fff;font-weight:600;font-size:6.5px;line-height:11px}
.band-left{left:0;width:110px;text-align:center}
.band-right{right:0;width:112px;text-align:center}
.party{font-size:7.5px;font-weight:400}

/* body pages */
.section-heading{font-size:6.2px;font-weight:600;margin:14px 0 10px 14px}
.section-heading:first-child{margin-top:4px}
.lead{font-size:5.7px;line-height:8px;margin:0 0 8px 14px}
.bullet{position:relative;padding-left:38px;font-size:5.7px;line-height:8px;margin-bottom:4px}
.bullet::before{content:"";position:absolute;left:16px;top:3px;width:3px;height:3px;border-radius:50%;background:var(--ink)}
.clause{position:relative;padding-left:38px;font-size:5.7px;line-height:8px;margin-bottom:11px}
.clause .num{position:absolute;left:0;top:1px;width:22px;height:7px;background:var(--ink);color:#fff;font-size:4.5px;line-height:7px;text-align:right;padding-right:3px;font-weight:400}
.clause.large{font-size:8px;line-height:11.5px;font-weight:400;margin-bottom:14px}
.item{position:relative;padding-left:62px;font-size:5.4px;line-height:7.5px;margin-bottom:10px}
.item .mark{position:absolute;left:40px;top:0}
.item.deep{padding-left:86px}
.item.deep .mark{left:62px}

/* signature page */
.witness{text-align:center;font-size:7.5px;line-height:14px;margin-top:4px}
.witness-date{font-size:7px;margin:0 0 0 16px}
.signatory{margin-left:192px;font-size:7px;font-weight:400}
.sig-row{display:flex;align-items:flex-end;gap:6px;margin-top:10px;font-size:7px}
.sig-line{width:93px;border-bottom:1px solid var(--ink);height:8px;margin-left:6px}
.seal-box{width:93px;height:35px;border:1px solid var(--ink);margin-left:auto}
.sig-block{margin-right:14px}
</style>
</head>
<body>
<div class="sheet">

  <!-- Cover -->
  <section class="page" style="left:529px;top:90px">
    <div class="cover-panel">
      <div class="cover-brand"><span class="brand-dot"></span><span>Meridane</span></div>
      <div class="cover-disc">NON-DISCLOSURE<br>AGREEMENT</div>
    </div>
  </section>

  <!-- Page 1 -->
  <section class="page" style="left:96px;top:690px">
    <div class="frame" style="padding:0">
      <div class="title-block doc-title">THIS NON-DISCLOSURE AGREEMENT<br><span class="doc-sub">('the Agreement')</span></div>
      <div class="dated-line">dated this _____________ day of _______________________________, __________</div>
      <div class="band band-left" style="top:228px">BETWEEN:</div>
      <div class="title-block party" style="top:270px">ACME of 118 Harbor Lane, CA, 95410, USA<br><span class="doc-sub">(the 'Company')</span></div>
      <div class="band band-right" style="top:312px">OF THE FIRST PART</div>
      <div class="band band-left" style="top:343px">AND</div>
      <div class="title-block party" style="top:387px">COMPANY NAME of COMPANY ADDRESS<br><span class="doc-sub">(the 'Evaluator')</span></div>
      <div class="band band-right" style="top:421px">OF THE SECOND PART</div>
    </div>
    <div class="page-footer"><div class="footer-brand"><span class="footer-dot"></span>Meridane</div><div class="page-number">1</div></div>
  </section>

  <!-- Page 2 -->
  <section class="page" style="left:529px;top:690px">
    <div class="frame">
      <h2 class="section-heading">BACKGROUND:</h2>
      <p class="bullet">ACME has proprietary information and know-how relating to certain investigation tools and tactics (the 'Company').</p>
      <p class="bullet">In connection with the Evaluator evaluating the Invention for possible patent, development, and marketing (the 'Permitted Purpose'), the Evaluator has requested certain confidential information (the 'Confidential Information') regarding the Company.</p>
      <p class="lead">IN CONSIDERATION OF and as a condition of the Company providing the Confidential Information to the Evaluator in addition to other valuable consideration, the receipt and sufficiency of which consideration is hereby acknowledged, the parties to this Agreement agree as follows:</p>
      <h2 class="section-heading" style="margin-top:20px">Confidential Information</h2>
      <p class="clause"><span class="num">1.</span>All written and oral information and materials disclosed or provided by the Company to the Evaluator under this Agreement constitute Confidential Information regardless of whether such information was provided before or after the date of this Agreement or how it was provided to the Evaluator.</p>
      <p class="clause"><span class="num">2.</span>'Confidential Information' means all data and information relating to the Invention as well as data and information relating to the Company, including but not limited to, the following:</p>
      <p class="item"><span class="mark">a.</span>'Business Operations' which includes internal personnel and financial information of the Company, vendor names and other vendor information, purchasing and internal cost information, internal services and operational manuals, external business contacts including those stored on social media accounts or similar platforms, and the manner and methods of conducting the Company's business;</p>
      <p class="item"><span class="mark">b.</span>'Customer Information' which includes names of customers of the Company, their representatives, all customer contact information, contracts and their contents and parties, customer services, data provided by customers and the type, quantity and specifications of products and services purchased, leased, licensed or received by customers of the Company;</p>
      <p class="item"><span class="mark">c.</span>'Intellectual Property' which includes information relating to the Company's proprietary rights prior to any public disclosure of such information, including but not limited to the nature of the proprietary rights, production data, technical and engineering data, technical concepts, test data and test results, simulation results, the status and details of research and development of products and services, and information regarding acquiring, protecting, enforcing and licensing proprietary rights (including patents, copyrights and trade secrets);</p>
    </div>
    <div class="page-footer"><div class="footer-brand"><span class="footer-dot"></span>Meridane</div><div class="page-number">2</div></div>
  </section>

  <!-- Page 3 -->
  <section class="page" style="left:963px;top:690px">
    <div class="frame">
      <p class="item"><span class="mark">d.</span>'Service Information' which includes all data and information relating to the services provided by the Company, including but not limited to, plans, schedules, manpower, inspection, and training information;</p>
      <p class="item" style="margin-top:14px"><span class="mark">e.</span>'Product Information' which includes all specifications for products of the Company as well as work product resulting from or related to work or projects of the Company, of any type or form in any stage of actual or anticipated research and development;</p>
      <p class="item" style="margin-top:14px"><span class="mark">f.</span>'Production Processes' which includes processes used in the creation, production and manufacturing of the work product of the Company, including but not limited to, formulas, patterns, molds, models, methods, techniques, specifications, processes, procedures, equipment, devices, programs, and designs;</p>
      <p class="item" style="margin-top:14px"><span class="mark">g.</span>'Accounting Information' which includes, without limitation, all financial statements, annual reports, balance sheets, company asset information, company liability information, revenue and expense reporting, profit and loss reporting, cash flow reporting, accounts receivable, accounts payable, Company reporting, purchasing information and payroll information of the Company;</p>
      <p class="item" style="margin-top:14px"><span class="mark">h.</span>'Marketing and Development Information' which includes marketing and development plans of the Company, price and cost data, price and fee amounts, pricing and billing policies, quoting procedures, marketing techniques and methods of obtaining business, forecasts and forecast assumptions and volumes, and future plans and potential strategies of the Company which have been or are being discussed;</p>
      <p class="item" style="margin-top:14px"><span class="mark">i.</span>'Computer Technology' which includes all scientific and technical information or material of the Company, pertaining to any machine, appliance or process, including but not limited to, specifications, proposals, models, designs, formulas, test results and reports, analyses, simulation results, tables of operating conditions, materials, components, industrial skills, operating and testing procedures, shop practices, know-how and show-how;</p>
      <p class="item" style="margin-top:14px"><span class="mark">j.</span>'Proprietary Computer Code' which includes all sets of statements, instructions or programs of the Company, whether in human readable or machine readable form, that are expressed, fixed, embodied or stored in any manner and that can be used directly or indirectly in a computer (Computer Programs); any report format, design or drawing created or produced by such Computer Programs; and all documentation, design specifications and charts, and operating procedures which support the Computer Programs; and</p>
      <p class="item" style="margin-top:14px"><span class="mark">k.</span>Confidential Information will also include any information that has been disclosed by a third party to the Company and is protected by a non-disclosure agreement entered into between the third party and the Company.</p>
    </div>
    <div class="page-footer"><div class="footer-brand"><span class="footer-dot"></span>Meridane</div><div class="page-number">3</div></div>
  </section>

  <!-- Page 4 -->
  <section class="page" style="left:96px;top:1290px">
    <div class="frame">
      <p class="clause"><span class="num">3.</span>Confidential Information will not include the following information:</p>
      <p class="item" style="margin-top:16px"><span class="mark">a.</span>Information that is generally known in the industry of the Company;</p>
      <p class="item"><span class="mark">b.</span>Information that is now or subsequently becomes generally available to the public through no wrongful act of the Evaluator;</p>
      <p class="item"><span class="mark">c.</span>Information rightly in the possession of the Evaluator prior to the disclosure to the Evaluator by the Company;</p>
      <p class="item"><span class="mark">d.</span>Information that is independently created by the Evaluator without direct or indirect use of the Confidential Information; or</p>
      <p class="item"><span class="mark">e.</span>Information that the Evaluator rightfully obtains from a third party who has the right to transfer or disclose it.</p>
      <h2 class="section-heading">OBLIGATIONS OF NON-DISCLOSURE</h2>
      <p class="clause"><span class="num">4.</span>Except as otherwise provided in this Agreement, the Evaluator must not disclose the Confidential Information.</p>
      <p class="clause"><span class="num">5.</span>Except as otherwise provided in this Agreement, the Confidential Information will remain the exclusive property of the Company and will only be used by the Evaluator for the Permitted Purpose. The Evaluator will not use the Confidential Information for any purpose that might be directly or indirectly detrimental to the Company or any associated affiliates or subsidiaries.</p>
      <p class="clause"><span class="num">6.</span>The obligations to ensure and prevent the disclosure of the Confidential Information imposed on the Evaluator in this Agreement and any obligations to provide notice under this Agreement will survive the expiration or termination, as the case may be, of this Agreement and those obligations will last indefinitely.</p>
      <p class="clause"><span class="num">7.</span>The Evaluator may disclose any of the Confidential Information:</p>
      <p class="item" style="margin-top:16px"><span class="mark">a.</span>to such employees, agents, representatives and advisors of the Evaluator that have a need to know for the Permitted Purpose provided that:</p>
    </div>
    <div class="page-footer"><div class="footer-brand"><span class="footer-dot"></span>Meridane</div><div class="page-number">4</div></div>
  </section>

  <!-- Page 5 -->
  <section class="page" style="left:529px;top:1290px">
    <div class="frame">
      <p class="item deep"><span class="mark">i.</span>the Evaluator has informed such personnel of the confidential nature of the Confidential Information;</p>
      <p class="item deep"><span class="mark">ii.</span>such personnel agree to be legally bound to the same burdens of non-disclosure and non-use as the Evaluator;</p>
      <p class="item deep"><span class="mark">iii.</span>the Evaluator agrees to take all necessary steps to ensure that the terms of this Agreement are not violated by such personnel; and</p>
      <p class="item deep"><span class="mark">iv.</span>the Evaluator agrees to be responsible for and indemnify the Company for any breach of this Agreement by its personnel.</p>
      <p class="item" style="margin-top:26px;margin-bottom:4px"><span class="mark">b.</span>to a third party where the Company has consented in writing to such disclosure; and</p>
      <p class="item"><span class="mark">c.</span>to the extent required by law or by the request or requirement of any judicial, legislative, administrative or other governmental body.</p>
      <p class="clause" style="margin-top:16px"><span class="num">8.</span>The Evaluator agrees to retain all Confidential Information at its usual place of business and to store all Confidential Information separate from other information and documents held in the same location. Further, the Confidential Information may not be used, reproduced, transformed, or stored on a computer or device that is accessible to persons to whom disclosure may not be made, as set out in this Agreement.</p>
      <h2 class="section-heading">NON-SOLICITATION</h2>
      <p class="clause"><span class="num">9.</span>The Evaluator, its affiliates, subsidiaries and representatives will not, from the date of this Agreement for a period of two years, directly or indirectly solicit for employment or employ any person who is now employed or retained by the Company or any affiliate of the Company without the prior written consent of the Company.</p>
      <h2 class="section-heading">NON-COMPETITION</h2>
      <p class="clause"><span class="num">10.</span>Other than with the express written consent of the Company, which consent may not be unreasonably withheld, the Evaluator will not, from the date of this Agreement for a period of two years, be directly or indirectly involved with a business which is in direct competition with the Company in the market for the Invention.</p>
      <h2 class="section-heading">OWNERSHIP AND TITLE</h2>
      <p class="clause"><span class="num">11.</span>Nothing contained in this Agreement will grant to or create in the Evaluator, either expressly or impliedly, any right, title, interest or license in or to the intellectual property of the Company.</p>
    </div>
    <div class="page-footer"><div class="footer-brand"><span class="footer-dot"></span>Meridane</div><div class="page-number">5</div></div>
  </section>

  <!-- Page 6 -->
  <section class="page" style="left:963px;top:1290px">
    <div class="frame">
      <h2 class="section-heading">REMEDIES</h2>
      <p class="clause"><span class="num">12.</span>The Evaluator agrees and acknowledges that the Confidential Information is of a proprietary and confidential nature and that any disclosure of the Confidential Information to a third party in breach of this Agreement cannot be reasonably or adequately compensated for in money damages and would cause irreparable injury to the Company. Accordingly, the Evaluator agrees that the Company is entitled to, in addition to all other rights and remedies available to it at law or in equity, an injunction restraining the Evaluator, any of its personnel, and any agents of the Evaluator, from directly or indirectly committing or engaging in any act restricted by this Agreement in relation to the Confidential Information.</p>
      <h2 class="section-heading" style="margin-top:22px">RETURN OF CONFIDENTIAL INFORMATION</h2>
      <p class="clause"><span class="num">13.</span>The Company may at any time request the return of all Confidential Information from the Evaluator. Upon the request of the Company, or in the event that the Evaluator ceases to require use of the Confidential Information, or upon the expiration or termination of this Agreement, the Evaluator will:</p>
      <p class="item" style="margin-bottom:4px"><span class="mark">a.</span>return all Confidential Information to the Company;</p>
      <p class="item"><span class="mark">b.</span>provide a certificate to the Company to the effect that the Evaluator has returned all Confidential Information to the Company.</p>
      <h2 class="section-heading" style="margin-top:18px">NOTICES</h2>
      <p class="clause"><span class="num">14.</span>In the event that the Evaluator is required in a civil, criminal or regulatory proceeding to disclose any part of the Confidential Information, the Evaluator will give to the Company prompt written notice of such request so the Company may seek an appropriate remedy or alternatively to waive the Evaluator's compliance with the provisions of this Agreement in regards to the request.</p>
      <p class="clause" style="margin-top:16px"><span class="num">15.</span>If the Evaluator loses or makes unauthorized disclosure of any of the Confidential Information, the Evaluator will immediately notify the Company and take all reasonable steps necessary to retrieve the lost or improperly disclosed Confidential Information.</p>
      <p class="clause"><span class="num">16.</span>Any notices or delivery required in this Agreement will be deemed completed when hand-delivered, delivered by agent, or seven days after being placed in the post, postage prepaid, to the parties at the addresses contained in this Agreement or as the parties may later designate in writing.</p>
      <p class="clause"><span class="num">17.</span>The addresses for any notice to be delivered to any of the parties to this Agreement are as follows:</p>
    </div>
    <div class="page-footer"><div class="footer-brand"><span class="footer-dot"></span>Meridane</div><div class="page-number">6</div></div>
  </section>

  <!-- Page 7 -->
  <section class="page" style="left:96px;top:1888px">
    <div class="frame">
      <p class="item"><span class="mark">a.</span><strong style="font-weight:600">Name:</strong> ACME<br><strong style="font-weight:600">Address:</strong> 902 Linden Ave, Fairview, MI 49000, USA</p>
      <p class="item" style="margin-top:16px"><span class="mark">b.</span><strong style="font-weight:600">Name:</strong> COMPANY NAME<br><strong style="font-weight:600">Address:</strong> COMPANY ADDRESS</p>
      <h2 class="section-heading" style="margin-top:18px">REPRESENTATIONS</h2>
      <p class="clause"><span class="num">18.</span>In providing the Confidential Information, the Company makes no representations, either expressly or impliedly as to its adequacy, sufficiency, completeness, correctness or its lack of defect of any kind, including any patent or trademark infringement that may result from the use of such information.</p>
      <h2 class="section-heading" style="margin-top:18px">FURTHER AGREEMENTS</h2>
      <p class="clause"><span class="num">19.</span>In the event that the Evaluator finds that the Invention is worthy of being patented, developed and marketed, the Company and the Evaluator may negotiate an additional agreement to define all their respective rights regarding such patenting, marketing, and development.</p>
      <h2 class="section-heading" style="margin-top:18px">TERMINATION</h2>
      <p class="clause"><span class="num">20.</span>Either party may terminate this Agreement by providing written notice to the other party. Except as otherwise provided in this Agreement, all rights and obligations under this Agreement will terminate at that time.</p>
      <h2 class="section-heading" style="margin-top:18px">ASSIGNMENT</h2>
      <p class="clause"><span class="num">21.</span>Except where a party has changed its corporate name or merged with another corporation, this Agreement may not be assigned or otherwise transferred by either party in whole or part without the prior written consent of the other party to this Agreement.</p>
      <h2 class="section-heading" style="margin-top:18px">AMENDMENTS</h2>
      <p class="clause"><span class="num">22.</span>This Agreement may only be amended or modified by a written instrument executed by both the Company and the Evaluator.</p>
    </div>
    <div class="page-footer"><div class="footer-brand"><span class="footer-dot"></span>Meridane</div><div class="page-number">7</div></div>
  </section>

  <!-- Page 8 -->
  <section class="page" style="left:529px;top:1888px">
    <div class="frame">
      <h2 class="section-heading">GOVERNING LAW</h2>
      <p class="clause"><span class="num">23.</span>This Agreement will be construed in accordance with and governed by the laws of the State of Michigan.</p>
      <h2 class="section-heading" style="margin-top:18px">GENERAL PROVISIONS</h2>
      <p class="clause"><span class="num">24.</span>Time is of the essence in this Agreement.</p>
      <p class="clause"><span class="num">25.</span>This Agreement may be executed in counterpart.</p>
      <p class="clause"><span class="num">26.</span>Headings are inserted for the convenience of the parties only and are not to be considered when interpreting this Agreement. Words in the singular mean and include the plural and vice versa. Words in the masculine mean and include the feminine and vice versa.</p>
      <p class="clause"><span class="num">27.</span>The clauses, paragraphs, and subparagraphs contained in this Agreement are intended to be read and construed independently of each other. If any part of this Agreement is held to be invalid, this invalidity will not affect the operation of any other part of this Agreement.</p>
      <p class="clause"><span class="num">28.</span>The Evaluator is liable for all costs, expenses and expenditures including, and without limitation, the complete legal costs incurred by the Company in enforcing this Agreement as a result of any default of this Agreement by the Evaluator.</p>
      <p class="clause"><span class="num">29.</span>The Company and the Evaluator acknowledge that this Agreement is reasonable, valid and enforceable. However, if a court of competent jurisdiction finds any of the provisions of this Agreement to be too broad to be enforceable, it is the intention of the Company and the Evaluator that such provision be reduced in scope by the court only to the extent deemed necessary by that court to render the provision reasonable and enforceable, bearing in mind that it is the intention of the Evaluator to give the Company the broadest possible protection against disclosure of the Confidential Information.</p>
      <p class="clause large"><span class="num">30.</span>No failure or delay by the Company in exercising any power, right or privilege provided in this Agreement will operate as a waiver, nor will any single or partial exercise of such rights, powers or privileges preclude any further exercise of them or the exercise of any other right, power or privilege provided in this Agreement.</p>
      <p class="clause large"><span class="num">31.</span>This Agreement will inure to the benefit of and be binding upon the respective heirs, executors, administrators, successors and assigns, as the case may be, of the Company and the Evaluator.</p>
      <p class="clause large"><span class="num">32.</span>This Agreement constitutes the entire agreement between the parties and there are no further items or provisions, either oral or otherwise.</p>
    </div>
    <div class="page-footer"><div class="footer-brand"><span class="footer-dot"></span>Meridane</div><div class="page-number">8</div></div>
  </section>

  <!-- Page 9 -->
  <section class="page" style="left:963px;top:1888px">
    <div class="frame">
      <p class="witness">IN WITNESS WHEREOF ACME and COMPANY NAME have duly<br>affixed their signatures under hand and seal</p>
      <p class="witness-date">on this ______________ day of ______________________________, __________.</p>
      <div class="sig-block" style="margin-top:58px">
        <p class="signatory">ACME</p>
        <div class="sig-row" style="margin-left:192px">Per:<span class="sig-line"></span></div>
        <div class="sig-row" style="margin-left:192px;align-items:flex-start">(Seal)<span class="seal-box"></span></div>
      </div>
      <div class="sig-block" style="margin-top:74px">
        <p class="signatory">COMPANY NAME</p>
        <div class="sig-row" style="margin-left:192px">Per:<span class="sig-line"></span></div>
        <div class="sig-row" style="margin-left:192px;align-items:flex-start">(Seal)<span class="seal-box"></span></div>
      </div>
    </div>
    <div class="page-footer"><div class="footer-brand"><span class="footer-dot"></span>Meridane</div><div class="page-number">9</div></div>
  </section>

</div>
</body>
</html>
```